Construction Site Sign

4' high x 8' wide construction site sign using the attached logo (small correction required) Utilize the red, white and blue colors; add the company address, telephone numbers and website.

58 Fenwick Mill Road, Suite 4
Crawford, Georgia 30630
(706) 318-2946 Office
(706) 561-3082 Fax
www.hollowbrookbuilders.biz

```html
<!DOCTYPE html>
<html lang="en">
<head>
<meta charset="utf-8">
<title>Hollowbrook Builders Inc – Construction Site Sign</title>
<link rel="stylesheet" href="https://fonts.googleapis.com/css2?family=Roboto:wght@400;700&family=Roboto+Condensed:wght@700&display=swap">
<style>
  :root {
    --page: #e8e9eb;
    --sign-white: #ffffff;
    --sky-top: #8fcbe9;
    --sky-mid: #c9e6f5;
    --flag-red: #e4222b;
    --flag-blue: #1b4fa0;
    --ink: #1c1c1c;
    --white: #ffffff;
  }
  * { box-sizing: border-box; margin: 0; padding: 0; }
  html, body {
    width: 1200px;
    height: 1000px;
    overflow: hidden;
    background: var(--page);
  }
  .site-sign {
    position: absolute;
    left: 49px;
    top: 260px;
    width: 1102px;
    height: 481px;
    background: var(--sign-white);
    box-shadow: 0 4px 14px rgba(0,0,0,0.18);
    overflow: hidden;
  }
  .sky-backdrop {
    position: absolute;
    inset: 0 0 76px 0;
    background: linear-gradient(180deg, var(--sky-top) 0%, var(--sky-mid) 38%, var(--sign-white) 78%);
  }
  .company-name {
    position: absolute;
    left: 0;
    right: 0;
    top: 170px;
    display: flex;
    align-items: center;
    justify-content: center;
    gap: 16px;
    font-family: "Roboto", Arial, sans-serif;
    font-weight: 700;
    font-size: 54px;
    letter-spacing: 1px;
    color: var(--flag-blue);
  }
  .company-name .name-mark {
    width: 30px;
    height: 30px;
    background: var(--flag-red);
  }
  .site-address {
    position: absolute;
    left: 0;
    right: 0;
    top: 430px;
    transform: translateY(-96px);
    text-align: center;
    font-family: "Roboto", Arial, sans-serif;
    font-weight: 400;
    font-size: 24px;
    color: var(--ink);
  }
  .contact-band {
    position: absolute;
    left: 0;
    bottom: 0;
    width: 1102px;
    height: 76px;
  }
  .contact-band svg {
    position: absolute;
    inset: 0;
  }
  .band-text {
    position: absolute;
    top: 0;
    height: 76px;
    display: flex;
    align-items: center;
    justify-content: center;
    font-family: "Roboto Condensed", "Arial Narrow", sans-serif;
    font-weight: 700;
    color: var(--white);
  }
  .band-web { left: 0; width: 445px; font-size: 27px; }
  .band-phones { left: 470px; width: 632px; font-size: 28px; }
</style>
</head>
<body>
  <main class="site-sign">
    <div class="sky-backdrop" role="img" aria-label="Photograph of a bright blue sky with soft white clouds"></div>

    <h1 class="company-name"><span class="name-mark"></span>HOLLOWBROOK BUILDERS INC</h1>

    <p class="site-address">58 Fenwick Mill Road, Suite 4 Crawford, Georgia 30630</p>

    <div class="contact-band">
      <svg width="1102" height="76" viewBox="0 0 1102 76" aria-hidden="true">
        <polygon points="0,0 440,0 462,38 440,76 0,76" fill="var(--flag-red)"/>
        <polygon points="458,0 1102,0 1102,76 458,76 480,38" fill="var(--flag-blue)"/>
      </svg>
      <div class="band-text band-web">www.hollowbrookbuilders.biz</div>
      <div class="band-text band-phones">(706) 318-2946 Office | (706) 561-3082 Fax</div>
    </div>
  </main>
</body>
</html>
```